Need a Zine cover designed

I’m looking for someone who can design an eye catching and original zine cover. Incorporating the logo I included below. I’m not 100% sure which logo I want to use on the cover, if it’s possible to see how you incorporate the logos on a sample will make it easier for me to decide. Thank you for your time.
For the second logo I’m unsure how to remove the grey background, but I do not want it included in the zine cover
The title of the zine is:
Amber Crossroads
perspectives of culture, life, & love

```html
<!DOCTYPE html>
<html lang="en">
<head>
<meta charset="utf-8">
<title>Amber Crossroads — Zine Cover</title>
<link rel="stylesheet" href="https://fonts.googleapis.com/css2?family=Bungee&family=Dancing+Script:wght@600&display=swap">
<style>
  :root {
    --backdrop: #dcdddf;
    --cover-dark: #0b0a09;
    --photo-warm: #2a1e17;
    --photo-deep: #120e0c;
    --title-lime: #d6df12;
    --brand-orange: #f08a24;
    --rule-white: #f2f2f2;
    --script-white: #ffffff;
  }
  * { margin: 0; padding: 0; box-sizing: border-box; }
  html, body {
    width: 1200px;
    height: 900px;
    overflow: hidden;
    background: var(--backdrop);
  }
  .canvas {
    position: relative;
    width: 1200px;
    height: 900px;
  }
  .zine-cover {
    position: absolute;
    left: 255px;
    top: 60px;
    width: 690px;
    height: 780px;
    background: var(--cover-dark);
    overflow: hidden;
    box-shadow: 0 18px 40px rgba(0, 0, 0, 0.25);
  }
  .cover-photo {
    position: absolute;
    inset: 0;
    background:
      radial-gradient(ellipse 55% 45% at 50% 60%, var(--photo-warm) 0%, transparent 75%),
      linear-gradient(160deg, var(--photo-deep) 0%, #1b1411 55%, var(--cover-dark) 100%);
    opacity: 0.9;
  }
  .cover-content {
    position: relative;
    display: flex;
    flex-direction: column;
    align-items: center;
    padding-top: 120px;
    height: 100%;
  }
  .brand-mark {
    display: flex;
    align-items: center;
    gap: 14px;
    font-family: "Bungee", sans-serif;
    font-size: 38px;
    line-height: 1;
    color: var(--brand-orange);
  }
  .brand-mark .brand-dot {
    width: 22px;
    height: 22px;
    border-radius: 50%;
    background: var(--brand-orange);
  }
  .title-rule {
    width: 150px;
    height: 2px;
    background: var(--rule-white);
  }
  .title-rule.top { margin-top: 70px; }
  .title-rule.bottom { margin-top: 30px; }
  .zine-title {
    margin-top: 30px;
    font-family: "Bungee", sans-serif;
    font-size: 86px;
    line-height: 0.95;
    color: var(--title-lime);
    text-align: center;
    text-transform: uppercase;
    letter-spacing: -1px;
  }
  .zine-subtitle {
    margin-top: 34px;
    font-family: "Dancing Script", cursive;
    font-weight: 600;
    font-size: 44px;
    line-height: 1.1;
    color: var(--script-white);
    text-align: center;
  }
</style>
</head>
<body>
  <main class="canvas">
    <section class="zine-cover">
      <div class="cover-photo" role="img" aria-label="Dark photograph of several hands stacked together in a team huddle"></div>
      <div class="cover-content">
        <div class="brand-mark">
          <span class="brand-dot"></span>
          <span class="brand-name">Breezewood Circle</span>
        </div>
        <div class="title-rule top"></div>
        <h1 class="zine-title">Amber<br>Crossroads</h1>
        <div class="title-rule bottom"></div>
        <p class="zine-subtitle">Perspectives of life<br>culture and love</p>
      </div>
    </section>
  </main>
</body>
</html>
```